Thermal Camera flyer

We would like to obtain a sales orientated brochure to promote our two models of thermal imaging cameras as a response to the current Covid 19 health issues. I have provided the text, photos and detailed product specifications , in addition to a sample competitors brochure.
BROCHURE Details : 2 sided - front side to show product, its applications in business, school, hospitals, with text details - Back page to show specifications chart and contact information for QT vista Works. (Melbourne -Sydney-Perth-Brisbane - 1300 847 519
Brochure should be "eye-catching" and reflect the product as a high quality, must-have technology device for todays world.

```html
<!DOCTYPE html>
<html lang="en">
<head>
<meta charset="utf-8">
<title>Thermal Scanning and Facial Recognition Camera – QT vista Works</title>
<link rel="stylesheet" href="https://fonts.googleapis.com/css2?family=Comfortaa:wght@700&family=Roboto:wght@300;400&family=Roboto+Condensed:wght@700&display=swap">
<style>
  :root {
    --paper: #dad8cf;
    --charcoal: #2a2630;
    --navy: #2b276a;
    --yellow-bright: #f3ec33;
    --yellow-olive: #dccf35;
    --title: #dcd9cc;
    --ink: #1f1d22;
    --blue: #2c55b2;
  }
  * { margin: 0; padding: 0; box-sizing: border-box; }
  html, body { width: 848px; height: 1200px; overflow: hidden; background: var(--paper); }
  .flyer {
    position: relative; width: 848px; height: 1200px; overflow: hidden;
    background: var(--paper); color: var(--ink);
    font-family: "Roboto", Arial, sans-serif; font-weight: 300;
  }
  .backdrop { position: absolute; inset: 0; }
  .product-photo { position: absolute; }
  .product-desk {
    left: 112px; top: 91px; width: 340px; height: 554px;
    border-radius: 40px 40px 60px 60px;
    background: radial-gradient(ellipse at 50% 40%, #3a3d48 0%, #1d1d22 55%, #111114 100%);
  }
  .product-stand {
    left: 320px; top: 768px; width: 170px; height: 432px;
    border-radius: 30px 30px 0 0;
    background: linear-gradient(160deg, #2b2b33 0%, #1c1c22 45%, #c9c9cc 75%, #e4e4e6 100%);
  }
  .title {
    position: absolute; left: 400px; top: 166px;
    font-family: "Comfortaa", "Varela Round", sans-serif; font-weight: 700;
    font-size: 44.5px; line-height: 50px; letter-spacing: -0.3px;
    color: var(--title);
  }
  .caption {
    position: absolute; left: 150px; width: 292px; top: 659px;
    text-align: center; font-size: 11.3px; font-weight: 300; color: var(--ink);
  }
  .intro {
    position: absolute; left: 83px; top: 735px; width: 218px;
    font-size: 17px; line-height: 19.3px; font-weight: 300;
  }
  .details {
    position: absolute; left: 502px; top: 558px; width: 264px;
    font-size: 12.2px; line-height: 15.1px; font-weight: 300;
  }
  .details h2 {
    font-family: "Roboto Condensed", "Arial Narrow", sans-serif; font-weight: 700;
    font-size: 12.6px; line-height: 15.2px; margin-bottom: 3px;
  }
  .details p { text-align: justify; margin-bottom: 4px; }
  .details p + h2 { margin-top: 6px; }
  .call {
    position: absolute; left: 502px; top: 1095px;
    font-family: "Roboto Condensed", "Arial Narrow", sans-serif; font-weight: 700;
    font-size: 25px; color: var(--blue); letter-spacing: -0.3px;
  }
  .brand {
    position: absolute; left: 81px; top: 1093px;
    display: flex; align-items: center; gap: 17px;
  }
  .brand-mark { width: 32px; height: 32px; background: var(--blue); }
  .brand-name { font-family: "Roboto", Arial, sans-serif; font-weight: 400; font-size: 20px; color: var(--charcoal); }
</style>
</head>
<body>
<main class="flyer">
  <svg class="backdrop" width="848" height="1200" viewBox="0 0 848 1200" aria-hidden="true">
    <rect width="848" height="1200" fill="var(--paper)"/>
    <path d="M0,0 H848 V470 C700,505 540,530 400,522 C240,512 90,480 0,455 Z" fill="var(--yellow-olive)"/>
    <path d="M0,55 C50,200 150,300 260,360 C180,380 80,390 0,395 Z" fill="var(--yellow-bright)"/>
    <path d="M848,165 C810,320 720,420 590,470 C700,460 790,440 848,420 Z" fill="var(--navy)"/>
    <path d="M0,0 H848 V170 C800,340 660,470 480,488 C300,500 110,300 0,63 Z" fill="var(--charcoal)"/>
    <path d="M420,1200 C520,1105 700,1062 848,1060 V1200 Z" fill="var(--yellow-olive)"/>
  </svg>

  <div class="product-photo product-desk" role="img" aria-label="Desktop thermal scanning camera on a black triangular base, screen showing a masked visitor with an admittance and body temperature reading"></div>

  <h1 class="title">Thermal<br>Scanning<br>and Facial<br>Recognition<br>Camera</h1>

  <p class="caption">Portable Camera for a Reception Desk</p>

  <p class="intro">The temperature of your body is no longer considered private information. That’s the stance that businesses around the world are taking as they install thermal imaging cameras for the safety of staff and visitors, often equipped with facial recognition technology, in their buildings in an attempt to cope with the COVID-19 pandemic. It’s a movement one might call the automation of temperature checks.</p>

  <div class="product-photo product-stand" role="img" aria-label="Floor-standing thermal scanning camera on a silver pedestal, screen showing a masked visitor admitted with a normal temperature"></div>

  <section class="details">
    <h2>The Purpose of Thermal Scanning<br>&amp; Facial Recognition</h2>
    <p>The purpose is to identify anyone walking into an establishment with a high temperature. This will reduce the likelihood of spreading any potential virus and brings some peace of mind to people in the building.</p>
    <p>We can pair your thermal camera/s with facial recognition software. Employees will check in by standing in front of the camera, which identifies them by their face in just a few seconds without contact (with or without a mask on) and simultaneously performs a thermal scan. It will record a photo of the individual, the date, the time and the temperature reading at that time of entering the building. If the camera detects a high temperature reading, it will sound an alarm in real time and send a notification to a nominated administrator/in-house security.</p>
    <h2>Where and how can it be used?</h2>
    <p>This Camera can be used with access control gates. It is used in office buildings, schools, hotels, hospitality, in fact, any space where Covid is potentially a threat to staff or visitors.</p>
    <p>Our Thermal Scanning &amp; Facial Recognition Camera is used as a safety and security measure.</p>
    <p>If someone gets sick and takes legal action, you can demonstrate that you have made your best effort to protect your staff and visitors.</p>
  </section>

  <div class="brand">
    <span class="brand-mark"></span>
    <span class="brand-name">QT vista Works</span>
  </div>

  <p class="call">Call : 1300 847 519</p>
</main>
</body>
</html>
```